Label for Whiskey and Rum Bottle

We are a distillery. Whiskey and Rum We like to have a new label for our bottles. The whiskey bottles are in a wooden case. http://www.kornfaesser.ch/store/product/talwinkel-obermatt-single-malt-whiskey-nr-6 The Rum Bottles have no package. The label is even more important. http://www.kornfaesser.ch/store/product/talwinkel-obermatter-rum You can see the form of the bottles here www.kornfaesser.ch/store Whiskey and rum bottles are for a liter (50 cl) The labels can be with a picture or without. We would like to have something completely new. Therefore we don`t like to make much prescriptions concerning the design. We don`t like to give too much information (text) on the label. Just the information required by law. Consumers should understand the labels without long-reading. (The label-text is below) The 2 labels (Whiskey and rum) should look similar. Probably they have a different color or a different picture or .... It should be clear that the 2 products are from the same distillery. We have the intention to change all our existing labels over time. This gives designers the chance for follow-up projects.

Target Market(s)

Adults, liquor lovers

Requirements
Must have
• Information on the label is in German. (See "") Whiskey: - the name of the whiskey is "Talwinkel Obermatt Single Malt Whiskey" - The Whiskey was matured 5 years in a sherry "5 years in the sherry barrel stored" - The Alcohol content is 40% volumes "40% Vol "- The bottle contents 50 cl" 5 dl "- The distillery is" Distillery Brunnacher, Tornwil, www.kornfaesser.ch "- The producer is" Kelvor GmbH "Rum: - The name is" Talwinkel Obermatter Rum "- The alcohol content is 37% Volumes "37% Vol" - The bottle contens 50 cl "5 dl" - The distillery is "Distillery Brunnacher, Tornwil, www.kornfaesser.ch" - The producer is "Kelvor GmbH"
Nice to have
• Premium looking label Only front label preferred Only necessary text on the label
Should not have
• No special print techniques necessary No special paper form

```html
<!DOCTYPE html>
<html lang="de">
<head>
<meta charset="utf-8">
<title>Talwinkel Obermatter – Etiketten Whiskey &amp; Rum</title>
<link rel="stylesheet" href="https://fonts.googleapis.com/css2?family=Cinzel:wght@600;700&family=Rye&display=swap">
<style>
  :root {
    --night: #0b0706;
    --paper: #ffffff;
    --gold: #b98a57;
    --gold-soft: rgba(185, 138, 87, 0.22);
    --cream: #f4f1ec;
    --ink-shadow: #4a4440;
    --navy: #1d4a85;
    --tan: #dcae82;
    --tan-soft: rgba(220, 174, 130, 0.25);
  }
  * { box-sizing: border-box; margin: 0; padding: 0; }
  html, body { width: 1200px; height: 991px; overflow: hidden; }
  body { display: flex; }
  .panel {
    width: 600px;
    height: 991px;
    display: flex;
    align-items: center;
    justify-content: center;
  }
  .panel--whiskey { background: var(--night); }
  .panel--rum { background: var(--paper); }
  .label { width: 570px; height: auto; display: block; }
  .label-title { font-family: "Rye", "Georgia", serif; }
  .label-small { font-family: "Cinzel", "Times New Roman", serif; font-weight: 700; }
</style>
</head>
<body>

<!-- Whiskey label -->
<section class="panel panel--whiskey">
  <svg class="label label--whiskey" viewBox="0 0 700 490" role="group" aria-label="Etikett Talwinkel Obermatt Single Malt Whiskey">
    <defs>
      <path id="w-top-arc" d="M172 88 Q330 14 488 88"/>
      <path id="w-info-arc" d="M210 398 Q335 445 470 398"/>
      <path id="w-address-arc" d="M185 414 Q335 482 495 414"/>
      <radialGradient id="w-ornament" cx="50%" cy="50%" r="50%">
        <stop offset="0%" stop-color="#b98a57" stop-opacity="0.32"/>
        <stop offset="100%" stop-color="#b98a57" stop-opacity="0"/>
      </radialGradient>
    </defs>

    <!-- ornament zones -->
    <ellipse class="ornament-crest" cx="330" cy="18" rx="40" ry="12" fill="url(#w-ornament)" role="img" aria-label="Kleine Zierkrone oben"/>
    <ellipse class="ornament-top" cx="330" cy="115" rx="200" ry="30" fill="url(#w-ornament)" role="img" aria-label="Filigrane Schnörkel über dem Namen"/>
    <ellipse class="ornament-left" cx="70" cy="240" rx="75" ry="150" fill="url(#w-ornament)" role="img" aria-label="Filigrane Schnörkel links"/>
    <ellipse class="ornament-right" cx="600" cy="240" rx="90" ry="150" fill="url(#w-ornament)" role="img" aria-label="Filigrane Schnörkel rechts"/>
    <ellipse class="ornament-bottom" cx="340" cy="375" rx="200" ry="28" fill="url(#w-ornament)" role="img" aria-label="Filigrane Schnörkel unter dem Namen"/>
    <ellipse class="ornament-foot" cx="335" cy="475" rx="35" ry="10" fill="url(#w-ornament)" role="img" aria-label="Kleine Zierkrone unten"/>

    <!-- frame lines -->
    <g class="frame" fill="none" stroke="var(--gold)" stroke-width="1.6">
      <path d="M140 68 Q330 0 520 68"/>
      <path d="M175 110 Q330 60 485 110" stroke="var(--cream)" stroke-width="1.2"/>
      <line x1="65" y1="122" x2="600" y2="122"/>
      <line x1="65" y1="128" x2="600" y2="128"/>
      <line x1="20" y1="155" x2="130" y2="155"/>
      <line x1="540" y1="155" x2="640" y2="155"/>
      <line x1="110" y1="345" x2="215" y2="345"/>
      <line x1="470" y1="345" x2="600" y2="345"/>
      <line x1="110" y1="352" x2="215" y2="352"/>
      <line x1="470" y1="352" x2="600" y2="352"/>
      <path d="M200 382 Q335 420 470 382" stroke="var(--cream)" stroke-width="1.2"/>
      <path d="M135 372 Q335 468 530 372"/>
    </g>

    <!-- arc text -->
    <text class="label-small" font-size="14" fill="var(--cream)" letter-spacing="1">
      <textPath href="#w-top-arc" startOffset="50%" text-anchor="middle">5 JAHRE IM SHERRY FASS GELAGERT</textPath>
    </text>

    <!-- title -->
    <text class="label-title" x="335" y="215" font-size="82" text-anchor="middle" textLength="380" lengthAdjust="spacingAndGlyphs"
          fill="var(--cream)" stroke="var(--ink-shadow)" stroke-width="7" paint-order="stroke">TALWINKEL</text>
    <text class="label-title" x="338" y="318" font-size="108" text-anchor="middle" textLength="650" lengthAdjust="spacingAndGlyphs"
          fill="var(--cream)" stroke="var(--ink-shadow)" stroke-width="8" paint-order="stroke">OBERMATT</text>

    <!-- product ribbon -->
    <rect x="220" y="326" width="245" height="32" fill="#2c2421" stroke="var(--gold)" stroke-width="1.4"/>
    <text class="label-small" x="342" y="348" font-size="14.5" text-anchor="middle" fill="var(--cream)" letter-spacing="1">SINGLE MALT WHISKEY</text>

    <!-- legal info -->
    <text class="label-small" font-size="12" fill="var(--cream)" letter-spacing="0.6">
      <textPath href="#w-info-arc" startOffset="50%" text-anchor="middle">KELVOR GMBH  |  40% VOL  |  5 DL</textPath>
    </text>
    <text class="label-small" font-size="8.4" fill="var(--cream)" letter-spacing="0.4">
      <textPath href="#w-address-arc" startOffset="50%" text-anchor="middle">BRENNEREI BRUNNACHER, TORNWIL, WWW.KORNFAESSER.CH</textPath>
    </text>
  </svg>
</section>

<!-- Rum label -->
<section class="panel panel--rum">
  <svg class="label label--rum" viewBox="0 0 700 490" role="group" aria-label="Etikett Talwinkel Obermatter Rum">
    <defs>
      <path id="r-info-arc" d="M210 398 Q335 445 470 398"/>
      <path id="r-address-arc" d="M185 414 Q335 482 495 414"/>
      <radialGradient id="r-ornament" cx="50%" cy="50%" r="50%">
        <stop offset="0%" stop-color="#dcae82" stop-opacity="0.4"/>
        <stop offset="100%" stop-color="#dcae82" stop-opacity="0"/>
      </radialGradient>
    </defs>

    <ellipse class="ornament-crest" cx="330" cy="18" rx="40" ry="12" fill="url(#r-ornament)" role="img" aria-label="Kleine Zierkrone oben"/>
    <ellipse class="ornament-top" cx="330" cy="115" rx="200" ry="30" fill="url(#r-ornament)" role="img" aria-label="Filigrane Schnörkel über dem Namen"/>
    <ellipse class="ornament-left" cx="70" cy="240" rx="75" ry="150" fill="url(#r-ornament)" role="img" aria-label="Filigrane Schnörkel links"/>
    <ellipse class="ornament-right" cx="600" cy="240" rx="90" ry="150" fill="url(#r-ornament)" role="img" aria-label="Filigrane Schnörkel rechts"/>
    <ellipse class="ornament-bottom" cx="340" cy="375" rx="200" ry="28" fill="url(#r-ornament)" role="img" aria-label="Filigrane Schnörkel unter dem Namen"/>
    <ellipse class="ornament-foot" cx="335" cy="475" rx="35" ry="10" fill="url(#r-ornament)" role="img" aria-label="Kleine Zierkrone unten"/>

    <g class="frame" fill="none" stroke="var(--tan)" stroke-width="1.6">
      <path d="M175 75 Q330 15 485 75" stroke="var(--navy)" stroke-width="1.8"/>
      <path d="M195 95 Q330 50 465 95" stroke="var(--navy)" stroke-width="1"/>
      <line x1="65" y1="122" x2="600" y2="122"/>
      <line x1="65" y1="128" x2="600" y2="128"/>
      <line x1="20" y1="155" x2="130" y2="155"/>
      <line x1="540" y1="155" x2="640" y2="155"/>
      <line x1="110" y1="345" x2="240" y2="345"/>
      <line x1="445" y1="345" x2="600" y2="345"/>
      <line x1="110" y1="352" x2="240" y2="352"/>
      <line x1="445" y1="352" x2="600" y2="352"/>
      <path d="M210 380 Q335 412 460 380" stroke="var(--navy)" stroke-width="1.4"/>
      <path d="M135 372 Q335 468 530 372"/>
    </g>

    <text class="label-title" x="335" y="215" font-size="82" text-anchor="middle" textLength="380" lengthAdjust="spacingAndGlyphs"
          fill="var(--navy)">TALWINKEL</text>
    <text class="label-title" x="338" y="318" font-size="108" text-anchor="middle" textLength="650" lengthAdjust="spacingAndGlyphs"
          fill="var(--navy)">OBERMATTER</text>

    <rect x="272" y="327" width="140" height="30" fill="var(--paper)" stroke="var(--tan)" stroke-width="1.4"/>
    <text class="label-small" x="342" y="348" font-size="15" text-anchor="middle" fill="var(--navy)" letter-spacing="2">RUM</text>

    <text class="label-small" font-size="12" fill="var(--navy)" letter-spacing="0.6">
      <textPath href="#r-info-arc" startOffset="50%" text-anchor="middle">KELVOR GMBH  |  37% VOL  |  5 DL</textPath>
    </text>
    <text class="label-small" font-size="8.4" fill="var(--navy)" letter-spacing="0.4">
      <textPath href="#r-address-arc" startOffset="50%" text-anchor="middle">BRENNEREI BRUNNACHER, TORNWIL, WWW.KORNFAESSER.CH</textPath>
    </text>
  </svg>
</section>

</body>
</html>
```